Natural Skincare Company Needs Label Design

We need a label design for the first product of a new company called 'Ovik'. We make skincare products made from natural ingredients.
Our initial product is a rose hip oil, and we need a label for the small 30mL bottle that it comes in, as well as for the box that the bottle will be sold in. The label will be printed directly onto the bottle, like the example in the attached photo. For reference, we like the look and feel of the labels on the bottle and box in the attached photos. It should convey a sense of natural.
The bottle will be dark green glass. For the name 'Ovik' we like something close to orange so that it stands out. The rest of the text on the front of the bottle and box should read 'natural skincare' 'pure & organic' 'Rose hip oil' 'huile de cynorrhodon' 'pure et biologique'. '30mL' '1fl.oz'
We also like the silhouette of the main ingredient like in the attached photo. So a silhouette of a rose hip on the front of the bottle and box would be preferred.
On the right side of the bottle and box:
'Rose hip oil'
'Ingredients: 100% natural, cold pressed, Rosa canina (rose hip) seed oil'
'Benefits: Hydrates and refreshes skin, leaving a more even skin tone and a healthy glow'
'Application: Massage 3-4 drops into clean, damp skin twice daily or as required'
'Suitable for all skin types'
'Store below 30C'
On the left side of the bottle and box:
'Huile de Cynorrhodon'
'Ingredients/Constituants: huile de Rosa canina (cynorrhodon) 100% naturel, presse a froid'
'Bienfaits: rafraichit la peau, teint eblouissant'
'Mode d'emploi: Massez 3 a 4 gouttes sur une peau propre et humide deluxe fois par jour'
'Convient a tous les types de peau'
'Conserver a moins de 30C'

```html
<!DOCTYPE html>
<html lang="en">
<head>
<meta charset="utf-8">
<title>Ovik Rose Hip Oil – Bottle Label</title>
<link href="https://fonts.googleapis.com/css2?family=Quicksand:wght@500;600&family=PT+Serif:wght@700&family=Yesteryear&display=swap" rel="stylesheet">
<style>
  :root{
    --paper:#f1f1f0;
    --glass:#3b5c17;
    --glass-deep:#2e4a0f;
    --cap:#262626;
    --orange:#f08a12;
    --ink:#ffffff;
    --rule:#d9e0cf;
    --leaf:rgba(38,58,14,.6);
  }
  *{margin:0;padding:0;box-sizing:border-box}
  html,body{width:1200px;height:1116px;overflow:hidden;background:var(--paper)}
  .canvas{position:relative;width:1200px;height:1116px;font-family:"Quicksand",sans-serif;color:var(--ink)}
  .cap{position:absolute;top:235px;width:110px;height:172px;background:var(--cap);border-radius:9px 9px 0 0}
  .cap--side{left:395px}
  .cap--front{left:695px}
  .bottle{position:absolute;top:404px;width:217px;height:478px;border-radius:38px 38px 40px 40px;
    background:linear-gradient(180deg,var(--glass) 0%,var(--glass-deep) 100%);overflow:hidden}
  .bottle--side{left:341px}
  .bottle--front{left:641px}

  /* side panel */
  .fact-tab{position:absolute;left:20px;top:86px;width:107px;height:25px;border:1px solid var(--rule);border-bottom:none;
    font-family:"PT Serif",serif;font-weight:700;font-size:12.5px;color:var(--orange);text-align:center;line-height:24px}
  .fact-table{position:absolute;left:20px;top:110px;width:178px;border:1px solid var(--rule)}
  .fact-row{border-top:1px solid var(--rule);padding:6px 9px 6px;font-size:8.6px;line-height:12px;font-weight:500}
  .fact-row:first-child{border-top:none}
  .fact-row h3{font-weight:500;font-size:9.5px;color:var(--orange);letter-spacing:.2px;line-height:12px}
  .fact-line{display:block;white-space:nowrap}
  .fact-line--full{text-align:justify;text-align-last:justify}
  .fact-row--note{color:var(--orange);padding:5px 9px 5px;height:24px}

  /* front panel */
  .brand-name{position:absolute;left:0;width:217px;top:52px;text-align:center;font-family:"Quicksand",sans-serif;
    font-weight:600;font-size:20px;color:var(--orange);line-height:1}
  .product-script{position:absolute;left:0;width:217px;top:88px;text-align:center;font-family:"Yesteryear",cursive;font-size:33px;color:var(--orange);line-height:1}
  .product-fr{position:absolute;left:41px;width:136px;top:125px;text-align:center;font-family:"PT Serif",serif;font-weight:700;font-size:8.2px;letter-spacing:.6px;
    padding-bottom:4px;border-bottom:1.5px solid var(--orange)}
  .ingredient-silhouette{position:absolute;left:100px;top:145px;width:125px;height:150px;border-radius:50% 30% 40% 60%;
    background:radial-gradient(ellipse at 55% 50%,var(--leaf),rgba(38,58,14,0) 72%)}
  .tagline{position:absolute;left:68px;top:160px;height:190px;writing-mode:vertical-rl;transform:rotate(180deg);
    font-size:15px;letter-spacing:1.3px;line-height:18px;text-align:left;font-weight:500}
  .claims{position:absolute;left:70px;top:356px;font-size:11px;line-height:14px;font-weight:500}
  .claims .en{color:var(--orange)}
  .volume{position:absolute;left:70px;top:448px;font-size:11px;letter-spacing:.6px;font-weight:500}
</style>
</head>
<body>
<main class="canvas">
  <div class="cap cap--side"></div>
  <section class="bottle bottle--side" aria-label="Side label">
    <div class="fact-tab">ROSE HIP OIL</div>
    <div class="fact-table">
      <div class="fact-row"><h3>INGREDIENTS</h3>
        <span class="fact-line fact-line--full">100% natural, cold pressed, Rosa</span>
        <span class="fact-line">canina (rose hip) seed oil.</span></div>
      <div class="fact-row"><h3>BENEFITS</h3>
        <span class="fact-line fact-line--full">Hydrates and refreshes skin,</span>
        <span class="fact-line fact-line--full">leaving a more even skin tone and</span>
        <span class="fact-line">a healthy glow.</span></div>
      <div class="fact-row"><h3>APPLICATION</h3>
        <span class="fact-line fact-line--full">Massage 3-4 drops into clean,</span>
        <span class="fact-line fact-line--full">damp skin twice daily or as re-</span>
        <span class="fact-line">quired.</span></div>
      <div class="fact-row fact-row--note">Suitable for all skin types.</div>
      <div class="fact-row fact-row--note">Store below 30C.</div>
    </div>
  </section>

  <div class="cap cap--front"></div>
  <section class="bottle bottle--front" aria-label="Front label">
    <div class="ingredient-silhouette" role="img" aria-label="Dark silhouette of a rose hip branch with leaves"></div>
    <div class="brand-name">Ovik</div>
    <div class="product-script">Rose Hip Oil</div>
    <div class="product-fr">HUILE DE CYNORRHODON</div>
    <div class="tagline">NATURAL SCINCARE</div>
    <div class="claims"><div class="en">PURE &amp; ORGANIC</div><div>PURE ET BIOLOGIQUE</div></div>
    <div class="volume">1 FL. OZ. / 30 ML</div>
  </section>
</main>
</body>
</html>
```